MODELS AGENCY NEW YEAR 2026 CARD

A 10 cm x 21 cm horizontal New Year card for clients of our 2 models agencies, Pommelin (kids) and Velvaride (actors and adults) (logo in the jobs).

Side A of the card: creative mission:
-text: 2026
-text: Peace and Love
-Studio or movie set atmosphere
-tone of voice: optimistic, positive, colorful

Side B:
(name of 4 people of the agency:)
Odette, Anne-Sophie, Hortense & Luc-Antoine,
(2 logos)
Pommelin & VelvaRide
(Adres)
Rue des Tilleuls 74 b3 - 1200 Bruxelles - Belgique

Target Market(s)

Movie directors, photographers

Industry/Entity Type

Fashion, advertising & Movies

Requirements
Must have
• SEE TEXT IN BRIEFING

```html
<!DOCTYPE html>
<html lang="en">
<head>
<meta charset="utf-8">
<title>New Year 2026 Card – Velvaride &amp; Pommelin</title>
<link rel="stylesheet" href="https://fonts.googleapis.com/css2?family=Playfair+Display:wght@900&family=Montserrat:wght@400;600;700&display=swap">
<style>
  :root {
    --board: #2d2d2d;
    --white: #ffffff;
    --ink: #111111;
    --navy-deep: #07073a;
    --indigo: #26208a;
    --violet: #4b2aa0;
    --magenta: #c8338a;
    --lavender: #d8dbf2;
    --steel: #5a5f70;
    --logo-purple: #4a2a6e;
    --logo-orange: #e8561c;
    --logo-blue: #1f9ad6;
  }
  * { box-sizing: border-box; margin: 0; padding: 0; }
  html, body {
    width: 1200px; height: 1200px; overflow: hidden;
    background: var(--board);
  }
  .board { position: relative; width: 1200px; height: 1200px; }

  /* Side A */
  .card-front {
    position: absolute; left: 98px; top: 114px; width: 1004px; height: 478px;
    overflow: hidden;
  }
  .front-photo {
    position: absolute; inset: 0;
    background:
      radial-gradient(ellipse 38% 30% at 45% 92%, rgba(200,51,138,0.85), transparent 70%),
      radial-gradient(ellipse 22% 25% at 84% 62%, rgba(200,51,138,0.75), transparent 70%),
      radial-gradient(ellipse 30% 40% at 55% 45%, rgba(75,42,160,0.8), transparent 75%),
      linear-gradient(100deg, var(--navy-deep) 0%, var(--indigo) 40%, var(--violet) 70%, var(--navy-deep) 100%);
  }
  .front-title {
    position: absolute; left: 0; right: 0; top: 92px;
    text-align: center; color: var(--white);
  }
  .year {
    font-family: "Playfair Display", serif; font-weight: 900;
    font-size: 212px; line-height: 1; letter-spacing: -4px;
  }
  .motto {
    margin-top: 8px;
    font-family: "Montserrat", sans-serif; font-weight: 400;
    font-size: 46px; line-height: 1; letter-spacing: 7px;
  }

  /* Side B */
  .card-back {
    position: absolute; left: 99px; top: 621px; width: 1001px; height: 476px;
    overflow: hidden; background: var(--white);
  }
  .back-photo {
    position: absolute; top: 0; right: 0; width: 62%; height: 100%;
    background:
      radial-gradient(ellipse 40% 45% at 60% 60%, rgba(30,30,40,0.85), transparent 75%),
      radial-gradient(ellipse 30% 35% at 78% 25%, rgba(40,40,50,0.7), transparent 75%),
      linear-gradient(90deg, var(--white) 0%, var(--lavender) 35%, var(--steel) 70%, #3a3d4a 100%);
  }
  .team, .address {
    position: absolute; left: 39px;
    font-family: "Montserrat", sans-serif; color: var(--ink);
    font-size: 19px; line-height: 23px;
  }
  .team { top: 37px; font-weight: 600; list-style: none; }
  .address { top: 139px; font-weight: 400; }

  .agencies {
    position: absolute; left: 46px; top: 363px;
    display: flex; gap: 40px; align-items: center;
  }
  .agency-name {
    font-family: "Montserrat", sans-serif; font-weight: 700;
    font-size: 22px; letter-spacing: 1px; color: var(--logo-purple);
    display: flex; align-items: center; gap: 8px;
  }
  .agency-dot { width: 12px; height: 12px; border-radius: 50%; }
  .agency-dot.adults { background: var(--logo-orange); }
  .agency-dot.kids { background: var(--logo-blue); }
</style>
</head>
<body>
<main class="board">
  <section class="card-front">
    <div class="front-photo" role="img" aria-label="Film studio set in silhouette with lights, tripods and crew, lit in deep blue and magenta"></div>
    <div class="front-title">
      <div class="year">2026</div>
      <div class="motto">PEACE AND LOVE</div>
    </div>
  </section>

  <section class="card-back">
    <div class="back-photo" role="img" aria-label="Camera operator looking through a cinema camera on set, fading into white"></div>
    <ul class="team">
      <li>Odette</li>
      <li>Anne-Sophie</li>
      <li>Hortense</li>
      <li>Luc-Antoine</li>
    </ul>
    <p class="address">Rue des Tilleuls 74 b3<br>- 1200 Bruxelles - Belgique</p>
    <div class="agencies">
      <div class="agency-name"><span class="agency-dot adults"></span>VELVARIDE</div>
      <div class="agency-name"><span class="agency-dot kids"></span>POMMELIN</div>
    </div>
  </section>
</main>
</body>
</html>
```